Auto Windschutzscheiben wechsel

Erstelle mir bitte eine Werbefolie, welches ich auf ein Auto kleben kann. Ich möchte was ausgefallenes und nichts langweiliges. Im Vordergrund soll die Windschutzscheibe stehen, dass jeder erkennt worum es geht. Damit will ich bewirken, dass die Leute die einen Steinschlag oder Riss haben, mich kontaktieren.

```html
<!DOCTYPE html>
<html lang="de">
<head>
<meta charset="utf-8">
<title>Glanzwerk – Fahrzeugfolie</title>
<link href="https://fonts.googleapis.com/css2?family=Exo+2:ital,wght@0,600;0,800;1,700&family=Oswald:wght@500&display=swap" rel="stylesheet">
<style>
  :root{
    --bg:#e9ecf3;
    --wrap:#141517;
    --wrap-2:#24262a;
    --blue:#2bb3e6;
    --red:#e8121c;
    --white:#f4f4f4;
    --photo-a:#c9d6df;
    --photo-b:#6d7f8c;
    --photo-c:#2c3338;
  }
  *{box-sizing:border-box;margin:0;padding:0}
  html,body{width:1200px;height:1200px;overflow:hidden;background:var(--bg)}
  body{position:relative;font-family:"Exo 2",sans-serif}

  .panel{position:absolute;overflow:hidden;background:linear-gradient(180deg,var(--wrap-2),var(--wrap) 60%);border-radius:10px}
  .panel--driver{left:40px;top:50px;width:1120px;height:460px}
  .panel--rear{left:40px;top:560px;width:440px;height:600px}
  .panel--passenger{left:510px;top:620px;width:650px;height:480px}

  .photo{position:absolute}
  .panel--driver .photo{left:540px;top:0;width:580px;height:300px;
    background:linear-gradient(90deg,transparent,var(--photo-b) 25%,var(--photo-a) 65%,var(--photo-b))}
  .panel--rear .photo{left:0;top:0;width:440px;height:420px;
    background:linear-gradient(180deg,var(--photo-a),var(--photo-b) 45%,var(--photo-c) 80%,transparent)}
  .panel--passenger .photo{left:0;top:0;width:380px;height:300px;
    background:linear-gradient(90deg,var(--photo-b),var(--photo-a) 40%,var(--photo-b) 75%,transparent)}

  .brand{position:absolute;text-align:center}
  .brand__name{font-weight:800;color:var(--white);text-transform:uppercase;line-height:1;letter-spacing:1px}
  .brand__tag{font-family:"Oswald",sans-serif;font-weight:500;color:var(--blue);display:flex;align-items:center;justify-content:center;gap:12px}
  .brand__tag::before,.brand__tag::after{content:"";height:2px;width:90px;background:var(--white);opacity:.8}
  .panel--driver .brand{left:270px;top:130px;width:520px}
  .panel--driver .brand__name{font-size:78px}
  .panel--driver .brand__tag{font-size:28px;margin-top:14px}
  .panel--passenger .brand{left:250px;top:110px;width:380px}
  .panel--passenger .brand__name{font-size:56px}
  .panel--passenger .brand__tag{font-size:22px;margin-top:10px}
  .panel--passenger .brand__tag::before,.panel--passenger .brand__tag::after{width:60px}
  .panel--rear .brand{left:20px;top:420px;width:190px}
  .panel--rear .brand__name{font-size:30px}
  .panel--rear .brand__tag{font-size:12px;margin-top:4px}
  .panel--rear .brand__tag::before,.panel--rear .brand__tag::after{width:30px;height:1px}

  .callout{position:absolute;display:flex;align-items:center;gap:6px}
  .callout__label{background:var(--red);color:var(--white);font-weight:800;text-transform:uppercase;padding:6px 14px;font-size:20px;border-radius:3px;white-space:nowrap}
  .panel--driver .callout{left:830px;top:140px}
  .panel--passenger .callout{left:20px;top:120px}
  .panel--rear .callout{left:40px;top:200px;flex-direction:column;align-items:flex-start}
  .panel--rear .callout__label{font-size:15px;padding:5px 10px}

  .benefits{position:absolute;list-style:none;color:var(--red);font-weight:800;text-transform:uppercase;line-height:1.05;white-space:nowrap}
  .benefits li{position:relative;margin-bottom:8px}
  .benefits li::after,.benefits li::before{content:"";position:absolute;top:7px;width:9px;height:9px;border-radius:50%;background:var(--red)}
  .panel--driver .benefits{right:50px;top:310px;text-align:right;font-size:21px}
  .panel--driver .benefits li::before{display:none}
  .panel--driver .benefits li::after{right:-22px}
  .panel--passenger .benefits{left:60px;top:320px;font-size:19px}
  .panel--passenger .benefits li::after{display:none}
  .panel--passenger .benefits li::before{left:-20px}
  .panel--rear .benefits{left:50px;top:292px;font-size:14px}
  .panel--rear .benefits li{margin-bottom:7px}
  .panel--rear .benefits li::after{display:none}
  .panel--rear .benefits li::before{left:-14px;top:4px;width:6px;height:6px}

  .contact-band{position:absolute;background:var(--blue);color:var(--wrap);font-weight:800;text-transform:uppercase;display:flex;align-items:center;white-space:nowrap}
  .phone{position:absolute;color:var(--white);font-weight:800;white-space:nowrap}
  .panel--driver .contact-band{left:0;top:330px;width:520px;height:44px;font-size:26px;padding-left:200px;clip-path:polygon(0 0,100% 0,96% 100%,0 100%)}
  .panel--driver .phone{left:190px;top:388px;font-size:40px}
  .panel--passenger .contact-band{right:0;top:300px;width:240px;height:38px;font-size:17px;padding-left:22px;clip-path:polygon(6% 0,100% 0,100% 100%,0 100%)}
  .panel--passenger .phone{right:12px;top:350px;font-size:26px}
  .panel--rear .contact-band{left:0;top:530px;width:440px;height:44px;font-size:17px;padding:0 14px;justify-content:space-between}
  .panel--rear .contact-band .url{background:var(--wrap);color:var(--white);padding:6px 10px;border-radius:0 14px 14px 0;margin-left:-14px}
</style>
</head>
<body>

<section class="panel panel--driver" aria-label="Fahrerseite">
  <div class="photo" role="img" aria-label="Foto: Monteure setzen eine neue Windschutzscheibe in einer Werkstatt ein, gesprungenes Glas im Vordergrund"></div>
  <div class="brand">
    <div class="brand__name">Glanzwerk</div>
    <div class="brand__tag">Car Painting</div>
  </div>
  <div class="callout">
    <svg width="90" height="44" viewBox="0 0 90 44" aria-hidden="true"><path d="M40 0H24L2 22l22 22h16L18 22zM80 0H64L42 22l22 22h16L58 22z" fill="var(--red)"/></svg>
    <span class="callout__label">Steinschlag?</span>
  </div>
  <ul class="benefits">
    <li>Kostenlose Abwicklung über die<br>Teilkasko - Versicherung</li>
    <li>Austausch erfolgt innerhalb<br>4 Stunden durch Profis</li>
    <li>Leihwagen inklusive</li>
  </ul>
  <div class="contact-band">glanzwerk-auto.de</div>
  <div class="phone">+49 151 2348190</div>
</section>

<section class="panel panel--rear" aria-label="Heck">
  <div class="photo" role="img" aria-label="Foto: zersprungene Heckscheibe eines Autos mit Blick in den Innenraum"></div>
  <div class="callout">
    <svg width="30" height="34" viewBox="0 0 30 34" aria-hidden="true"><path d="M0 16L15 0l15 16v10L15 10 0 26z" fill="var(--red)"/></svg>
    <span class="callout__label">Steinschlag?</span>
  </div>
  <ul class="benefits">
    <li>Kostenlose Abwicklung über die<br>Teilkasko Versicherung</li>
    <li>Austausch erfolgt innerhalb<br>4 Stunden durch Profis</li>
    <li>Leihwagen inklusive</li>
  </ul>
  <div class="brand">
    <div class="brand__name">Glanzwerk</div>
    <div class="brand__tag">Car Painting</div>
  </div>
  <div class="contact-band"><span class="url">glanzwerk-auto.de</span><span>+49 151 2348190</span></div>
</section>

<section class="panel panel--passenger" aria-label="Beifahrerseite">
  <div class="photo" role="img" aria-label="Foto: Monteure mit blauen Handschuhen heben eine Windschutzscheibe in einer Werkstatt"></div>
  <div class="callout">
    <span class="callout__label">Steinschlag?</span>
    <svg width="70" height="40" viewBox="0 0 70 40" aria-hidden="true"><path d="M0 0h14l20 20-20 20H0l20-20zM34 0h14l20 20-20 20H34l20-20z" fill="var(--red)"/></svg>
  </div>
  <div class="brand">
    <div class="brand__name">Glanzwerk</div>
    <div class="brand__tag">Car Painting</div>
  </div>
  <ul class="benefits">
    <li>Kostenlose Abwicklung über die<br>Teilkasko - Versicherung</li>
    <li>Austausch erfolgt innerhalb<br>4 Stunden durch Profis</li>
    <li>Leihwagen inklusive</li>
  </ul>
  <div class="contact-band">glanzwerk-auto.de</div>
  <div class="phone">+49 151 2348190</div>
</section>

</body>
</html>
```